Retractable Banner Design Featuring Key Product for Beauty Trade Show

We're a beauty/nail supply company that specializes in products used in professional nail salons. The key product for this design is Disposable Latex Gloves.
We will be exhibiting in a trade show this summer and are looking for a free-standing Retractable Banner Design that will be displayed at the front of our booth. The goal of the banner will be to display key products that are high in demand with our customers. The banner will be used to attract attention and highlight key selling points of these popular products. We would like the banner to be focused on the product title, image and key points, with a beauty/model/pattern background to create a professional appearance.
Nail Salons
Nail & Beauty Industry

```html
<!DOCTYPE html>
<html lang="en">
<head>
<meta charset="utf-8">
<title>Latex Gloves – Retractable Banner</title>
<link href="https://fonts.googleapis.com/css2?family=Merriweather:wght@900&family=Ubuntu:wght@700&family=Exo+2:wght@500;700;800&display=swap" rel="stylesheet">
<style>
  :root {
    --orange: #e8740c;
    --orange-deep: #c45f05;
    --ink: #2b2b2b;
    --dark-corner: #2f2f2f;
    --paper: #ffffff;
    --mist: #eeeeef;
    --backdrop: #e4e4e6;
  }
  html, body { margin: 0; padding: 0; overflow: hidden; }
  body {
    width: 982px; height: 1200px;
    background: var(--backdrop);
    font-family: "Exo 2", sans-serif;
    position: relative;
  }
  .banner {
    position: absolute; left: 271px; top: 10px;
    width: 440px; height: 1180px;
    background: linear-gradient(135deg, var(--mist), var(--paper) 45%, var(--mist));
    overflow: hidden;
  }
  .banner-shapes { position: absolute; inset: 0; }
  .title-latex {
    position: absolute; right: 52px; top: 70px; margin: 0;
    font-family: "Merriweather", serif; font-weight: 900;
    font-size: 58px; color: var(--ink); line-height: 1;
    text-shadow: 2px 2px 0 #c9c9c9;
  }
  .title-gloves {
    position: absolute; left: 54px; top: 128px; margin: 0;
    font-family: "Ubuntu", sans-serif; font-weight: 700;
    font-size: 100px; color: var(--orange); line-height: 1; letter-spacing: -2px;
    text-shadow: 3px 3px 0 #cfcfcf;
  }
  .photo { position: absolute; }
  .photo-hero {
    left: 0; top: 230px; width: 420px; height: 350px;
    border-radius: 0 0 120px 0;
    background: linear-gradient(150deg, #f1ece8 0%, #e8c2a4 38%, #f4f4f4 52%, #e67a1f 75%, #f6f6f6 100%);
  }
  .photo-inset {
    left: 282px; top: 720px; width: 128px; height: 128px; border-radius: 50%;
    background: linear-gradient(140deg, #f4f4f4, #e9e7e5 55%, #e2b89a);
  }
  .photo-box {
    left: 256px; top: 895px; width: 140px; height: 118px;
    background: linear-gradient(160deg, #f2f2f2 0%, #f2f2f2 45%, #e8740c 60%, #d8670a 100%);
  }
  .accent-bar { border-left: 3px solid var(--orange); padding-left: 12px; }
  .quantity {
    position: absolute; left: 49px; top: 632px;
    font-weight: 800; font-size: 25px; line-height: 1.35; color: #111;
  }
  .quantity .hl { color: var(--orange); }
  .key-title {
    position: absolute; left: 44px; top: 734px; margin: 0;
    font-weight: 800; font-size: 36px; color: var(--ink); line-height: 1;
  }
  .key-title .hl { color: var(--orange); }
  .key-list {
    position: absolute; left: 44px; top: 782px; margin: 0; padding: 0;
    list-style: none; width: 205px;
  }
  .key-list li {
    margin-bottom: 16px; font-size: 17px; line-height: 1.2; color: #111;
    font-weight: 500; white-space: nowrap;
  }
  .key-list .hl { display: block; color: var(--orange); font-weight: 700; }
  .call {
    position: absolute; left: 0; right: 0; top: 1068px; margin: 0;
    text-align: center; color: var(--paper);
    font-weight: 800; font-size: 40px; letter-spacing: 0.5px;
  }
</style>
</head>
<body>
  <section class="banner">
    <svg class="banner-shapes" width="440" height="1180" viewBox="0 0 440 1180">
      <polygon points="0,0 440,0 440,40 0,290" fill="var(--dark-corner)"/>
      <circle cx="250" cy="270" r="230" fill="var(--paper)"/>
      <path d="M 150 560 Q 330 560 440 470 L 440 540 Q 330 620 200 600 Z" fill="var(--orange)"/>
      <path d="M 0 1025 Q 160 1055 290 1035 L 440 1010 L 440 1180 L 0 1180 Z" fill="var(--orange)"/>
      <circle cx="335" cy="955" r="82" fill="var(--paper)"/>
      <circle cx="346" cy="784" r="72" fill="none" stroke="var(--orange)" stroke-width="1.2"/>
      <circle cx="282" cy="830" r="24" fill="var(--orange)"/>
    </svg>

    <div class="photo photo-hero" role="img" aria-label="Gloved hands pulling on a white latex glove beside a dispenser box and a case of latex gloves"></div>

    <h1 class="title-latex">Latex</h1>
    <h2 class="title-gloves">Gloves</h2>

    <div class="quantity accent-bar">
      Quantity: <span class="hl">(1,000 Pcs/Case),</span><br>(84 Cases Per Pallet)
    </div>

    <h3 class="key-title">KEY <span class="hl">POINTS:</span></h3>
    <ul class="key-list">
      <li class="accent-bar">100% Powder-Free –<span class="hl">no residue or irritants</span></li>
      <li class="accent-bar">Premium Textured<span class="hl">Grip for Superior Grip</span></li>
      <li class="accent-bar">6.2g Latex –<span class="hl">Super Heavy Duty</span></li>
      <li class="accent-bar">Designed for<span class="hl">Professional Salons!</span></li>
    </ul>

    <div class="photo photo-inset" role="img" aria-label="Hand pulling on a white latex glove"></div>
    <div class="photo photo-box" role="img" aria-label="Case of latex gloves, size small"></div>

    <p class="call">CALL: 1234 567 890</p>
  </section>
</body>
</html>
```